Web Design Project

Please design a new website template for Calderbrook as follows -

Existing Website - http://www.calderbrook.com.au/

Logo - http://rankyoursitenow.com/Design/calderbrook-logo

Navigation - Top Horizontal

Colours: Pink and purple from attached logo (do not use the bright pink from the existing website)

Page Structure: Home, About Us, Services, The Team, Key Contacts, Our Values, Send Resume, Timesheets, Candidates, Clients, Location, Contact Us.

The template should include an enquiry from on all pages with fields: Name, Phone, Email, Enquiry

The template should include their phone number in the top right corner - (08) 9271 5608

It should include a tag line: Temporary & Permanent Support Staff Specialists

The Footer:
Level 5, 7 Pemberly Terrace
SUBIACO
WA 6008
Phone - (08) 9271 5608
Fax - (08) 9271 5690
Email - admin@calderbrook.com.au

Websites they like - http://www.markdunwoodycosmeticclinic.com.au/ (preferably keep the text on a white background on this site)

Include a button/icon for - Job Listings

Home page text - Use what is on their existing website (you can reduce the number of bullet points)

```html
<!DOCTYPE html>
<html lang="en">
<head>
<meta charset="utf-8">
<title>Calderbrook – The Recruitment Bureau</title>
<link href="https://fonts.googleapis.com/css2?family=Oswald:wght@500;700&family=Arimo:wght@400;700&family=Cinzel:wght@400&display=swap" rel="stylesheet">
<style>
:root{
  --plum:#7d0f58;
  --plum-dark:#5e0741;
  --magenta:#b81d85;
  --pink-panel:#ec8cc4;
  --pink-wash:#f7e3ef;
  --ink:#1c1c1c;
  --charcoal:#262626;
  --news-bg:#e9eff2;
  --white:#ffffff;
}
*{box-sizing:border-box;margin:0;padding:0}
html,body{width:1107px;height:1200px;overflow:hidden;background:var(--white)}
body{position:relative;font-family:"Arimo",Arial,sans-serif;color:var(--ink);font-size:13px}
.abs{position:absolute}

/* header */
.site-header{left:0;top:0;width:1107px;height:138px;background:linear-gradient(180deg,#fff 0%,#fbf1f6 100%);border-top:4px dotted #222}
.brand{left:97px;top:64px;width:252px;display:flex;flex-direction:column;align-items:center}
.brand-name{font-family:"Cinzel",serif;font-size:31px;line-height:1;color:var(--plum);letter-spacing:.5px;white-space:nowrap}
.brand-sub{font-family:"Cinzel",serif;font-size:10px;color:var(--plum);letter-spacing:.6px;margin-top:4px}
.call{left:783px;top:44px;display:flex;align-items:center;gap:10px}
.call-text{font-family:"Oswald",sans-serif;color:#2b2b2b;line-height:1.05}
.call-text .label{font-size:18px;font-weight:500}
.call-text .number{font-size:25px;font-weight:700}

/* nav */
.main-nav{left:0;top:138px;width:1107px;height:39px;background:linear-gradient(180deg,#c02c8d 0%,#8c1462 100%)}
.main-nav ul{list-style:none;display:flex;position:absolute;left:98px;top:0;height:39px;align-items:center}
.main-nav li{color:#fff;font-size:13px;margin-right:15px;white-space:nowrap}
.main-nav li.current{background:linear-gradient(180deg,#4a4a4a,#1d1d1d);height:46px;margin-top:-6px;padding:18px 11px 0;border-radius:4px 4px 14px 14px;margin-right:18px;color:#eee}

/* hero */
.hero{left:0;top:177px;width:1107px;height:330px;background:linear-gradient(160deg,#fff 0%,#f3d3e5 45%,#fbeef5 75%,#fff 100%);overflow:hidden}
.hero-illustration{left:130px;top:10px;width:330px;height:270px;background:radial-gradient(ellipse at 50% 55%,#e6e6e6 0%,#f4f0f2 55%,rgba(255,255,255,0) 75%)}
.enquiry-head{left:676px;top:189px;width:351px;height:79px;background:linear-gradient(180deg,#3c3a3b,#1f1d1e);padding:7px 0 0 31px;color:#fff}
.enquiry-head h2{font-family:"Oswald",sans-serif;font-weight:700;font-size:25px;line-height:1.1}
.enquiry-head p{font-size:12.5px;line-height:1.35;margin-top:2px;padding-right:14px}
.enquiry-form{left:689px;top:262px;width:327px;height:216px;background:var(--pink-panel);border-radius:0 0 7px 7px;padding:6px 0 0 18px}
.field{display:flex;align-items:flex-start;margin-bottom:6px}
.field label{width:56px;font-weight:700;font-size:13px;padding-top:8px}
.field span{width:233px;height:31px;background:#fff;border-radius:4px;border:1px solid #d9a3c3;display:block}
.field.tall span{height:60px}
.callback{margin-left:56px;margin-top:3px;width:151px;height:30px;border-radius:15px;background:linear-gradient(180deg,#fff,#dcdcdc);border:1px solid #bbb;font-size:13px;color:#555;font-weight:700;display:flex;align-items:center;justify-content:center}

/* feature band */
.features{left:0;top:507px;width:1107px;height:114px;background:var(--charcoal);border-top:2px dashed #444;border-bottom:2px dashed #444}
.feature{top:0;height:110px;display:flex;align-items:center;gap:14px}
.feature h3{font-family:"Oswald",sans-serif;font-weight:700;color:#fff;font-size:23px;letter-spacing:.3px;white-space:nowrap}
.feature .more{display:inline-block;margin-top:4px;font-family:"Oswald",sans-serif;font-size:10px;font-weight:500;color:#444;background:linear-gradient(180deg,#fff,#cfcfcf);border-radius:3px;padding:2px 7px}
.divider{top:12px;width:1px;height:90px;background:#3a3a3a}

/* content */
.intro{left:92px;top:638px;width:645px}
.intro h1{font-family:"Oswald",sans-serif;font-weight:700;font-size:25px;color:#222}
.intro .tagline{color:var(--magenta);font-weight:700;font-size:16px;margin-top:22px}
.intro p{font-size:13px;line-height:1.55;margin-top:3px}
.areas{left:92px;top:782px;display:flex;gap:38px}
.areas ul{list-style:none;width:166px}
.areas ul + ul{width:230px}
.areas li{display:flex;align-items:center;gap:9px;height:23px;font-size:13px;white-space:nowrap}
.areas svg{flex:none}
.news{left:774px;top:636px;width:236px;height:292px;background:var(--news-bg);border:1px solid #d3dde2;border-radius:4px;padding:14px 17px}
.news h2{font-family:"Oswald",sans-serif;font-weight:700;color:var(--magenta);font-size:25px}
.news p{font-size:12.5px;line-height:1.33;text-align:justify;margin-top:6px;hyphens:auto}
.news a{display:inline-block;margin-top:14px;color:#222;font-size:12.5px;text-decoration:none;border-bottom:1px solid #222}

/* footer */
.site-footer{left:0;top:962px;width:1107px;height:238px;background:linear-gradient(180deg,#7b1259 0%,#5b0640 100%);color:#f4e4ee}
.footer-title{font-size:13px;letter-spacing:.3px;color:#fff;top:14px}
.footer-rule{left:0;top:39px;width:1107px;height:1px;background:rgba(255,255,255,.12)}
.map{left:92px;top:58px;width:168px;height:81px;background:linear-gradient(135deg,#efe8d8,#f2df8c 55%,#e8e2d2);border:1px solid #ddd}
.address{left:280px;top:58px;font-size:11.5px;line-height:1.6;letter-spacing:.3px}
.address b{color:#fff}
.links{list-style:none;font-size:11.5px;line-height:1.6;letter-spacing:.3px}
.links li::before{content:"› ";}
.follow{left:913px;top:54px;list-style:none;font-size:11.5px;letter-spacing:.3px}
.follow li{display:flex;align-items:center;gap:9px;height:29.5px}
.follow li span{width:22px;height:22px;border-radius:3px;background:#d8d0d6}
.copyright{left:0;top:211px;width:1107px;text-align:center;font-size:11.5px;color:#fff}
.footer-rule.bottom{top:200px}
</style>
</head>
<body>

<header class="site-header abs">
  <div class="brand abs">
    <span class="brand-name">CALDERBROOK</span>
    <span class="brand-sub">THE RECRUITMENT BUREAU</span>
  </div>
  <div class="call abs">
    <svg width="70" height="52" viewBox="0 0 70 52" aria-hidden="true">
      <rect x="12" y="22" width="46" height="26" rx="5" fill="#3a3a3a"/>
      <circle cx="35" cy="34" r="9" fill="#bbb" stroke="#222" stroke-width="2"/>
      <path d="M6 18 C6 4 64 4 64 18 L56 22 C52 16 18 16 14 22 Z" fill="#222"/>
    </svg>
    <div class="call-text">
      <div class="label">Call Us @</div>
      <div class="number">(08) 9271 5608</div>
    </div>
  </div>
</header>

<nav class="main-nav abs">
  <ul>
    <li class="current">Home</li><li>About Us</li><li>Services</li><li>The Team</li><li>Key Contacts</li><li>Our Values</li><li>Send Resume</li><li>Timesheets</li><li>Candidates</li><li>Clients</li><li>Location</li><li>Contact Us</li>
  </ul>
</nav>

<section class="hero abs">
  <svg class="abs" style="left:0;top:0" width="1107" height="330" aria-hidden="true">
    <path d="M0 220 C250 60 520 20 760 80 S1000 200 1107 150" fill="none" stroke="#d9a2c4" stroke-width="16" opacity=".55"/>
    <path d="M0 250 C300 110 560 60 800 120 S1020 230 1107 190" fill="none" stroke="#e7bdd6" stroke-width="6" opacity=".7"/>
    <path d="M0 30 C200 60 380 150 560 130" fill="none" stroke="#fff" stroke-width="3" opacity=".8"/>
  </svg>
  <div class="hero-illustration abs" role="img" aria-label="Illustration of people figures around puzzle pieces forming a team"></div>
</section>

<div class="enquiry-head abs">
  <h2>Find Out More</h2>
  <p>Complete this form and we'll get back to you within 24 hours to answer your questions.</p>
</div>
<form class="enquiry-form abs">
  <div class="field"><label>Name:</label><span></span></div>
  <div class="field"><label>Phone:</label><span></span></div>
  <div class="field"><label>Email:</label><span></span></div>
  <div class="field tall"><label>Enquiry:</label><span></span></div>
  <div class="callback">Request a Call Back</div>
</form>

<section class="features abs">
  <div class="feature abs" style="left:98px">
    <svg width="46" height="42" viewBox="0 0 46 42" aria-hidden="true"><rect x="15" y="2" width="16" height="8" rx="2" fill="none" stroke="#fff" stroke-width="3"/><rect x="1" y="9" width="44" height="32" rx="2" fill="#fff"/><rect x="1" y="20" width="44" height="3" fill="#262626"/></svg>
    <div><h3>JOB LISTINGS</h3><span class="more">READ MORE</span></div>
  </div>
  <div class="divider abs" style="left:323px"></div>
  <div class="feature abs" style="left:344px">
    <svg width="58" height="52" viewBox="0 0 58 52" aria-hidden="true"><circle cx="14" cy="14" r="10" fill="none" stroke="#fff" stroke-width="6" stroke-dasharray="4 3"/><circle cx="38" cy="34" r="13" fill="none" stroke="#fff" stroke-width="8" stroke-dasharray="5 3"/></svg>
    <div><h3>SERVICES</h3><span class="more">READ MORE</span></div>
  </div>
  <div class="divider abs" style="left:538px"></div>
  <div class="feature abs" style="left:556px">
    <svg width="76" height="50" viewBox="0 0 76 50" aria-hidden="true"><rect x="14" y="3" width="60" height="38" rx="3" fill="none" stroke="#fff" stroke-width="3"/><path d="M14 3 L44 26 L74 3" fill="none" stroke="#fff" stroke-width="3"/><circle cx="12" cy="37" r="10" fill="#fff"/><path d="M7 41 L12 32 L17 41" fill="none" stroke="#262626" stroke-width="2.5"/></svg>
    <div><h3>KEY CONTACTS</h3><span class="more">READ MORE</span></div>
  </div>
  <div class="divider abs" style="left:808px"></div>
  <div class="feature abs" style="left:834px">
    <svg width="52" height="42" viewBox="0 0 52 42" aria-hidden="true"><rect x="1" y="1" width="50" height="40" rx="6" fill="#fff"/><path d="M6 22 H18 L22 12 L27 32 L31 16 L34 22 H46" fill="none" stroke="#262626" stroke-width="2.5"/></svg>
    <div><h3>OUR VALUES</h3><span class="more">READ MORE</span></div>
  </div>
</section>

<section class="intro abs">
  <h1>Calderbrook - The Recruitment Bureau</h1>
  <div class="tagline">"Support Staff Specialists - Temporary and Permanent"</div>
  <p>Calderbrook has impeccable credentials. Our experienced and thoroughly professional team services a broad range of blue-chip national and multi-national companies with the recruitment of temporary and permanent staff in the areas of:</p>
</section>

<div class="areas abs">
  <ul>
    <li><svg width="18" height="14" viewBox="0 0 18 14"><path d="M1 7 H15 M9 1 L15 7 L9 13" fill="none" stroke="#b81d85" stroke-width="3"/></svg>Administration</li>
    <li><svg width="18" height="14" viewBox="0 0 18 14"><path d="M1 7 H15 M9 1 L15 7 L9 13" fill="none" stroke="#b81d85" stroke-width="3"/></svg>Personal Assistant</li>
    <li><svg width="18" height="14" viewBox="0 0 18 14"><path d="M1 7 H15 M9 1 L15 7 L9 13" fill="none" stroke="#b81d85" stroke-width="3"/></svg>Executive Assistant</li>
    <li><svg width="18" height="14" viewBox="0 0 18 14"><path d="M1 7 H15 M9 1 L15 7 L9 13" fill="none" stroke="#b81d85" stroke-width="3"/></svg>Reception</li>
    <li><svg width="18" height="14" viewBox="0 0 18 14"><path d="M1 7 H15 M9 1 L15 7 L9 13" fill="none" stroke="#b81d85" stroke-width="3"/></svg>Legal</li>
    <li><svg width="18" height="14" viewBox="0 0 18 14"><path d="M1 7 H15 M9 1 L15 7 L9 13" fill="none" stroke="#b81d85" stroke-width="3"/></svg>Secretaries</li>
    <li><svg width="18" height="14" viewBox="0 0 18 14"><path d="M1 7 H15 M9 1 L15 7 L9 13" fill="none" stroke="#b81d85" stroke-width="3"/></svg>Accounts Clerk</li>
  </ul>
  <ul>
    <li><svg width="18" height="14" viewBox="0 0 18 14"><path d="M1 7 H15 M9 1 L15 7 L9 13" fill="none" stroke="#b81d85" stroke-width="3"/></svg>Project Engineering</li>
    <li><svg width="18" height="14" viewBox="0 0 18 14"><path d="M1 7 H15 M9 1 L15 7 L9 13" fill="none" stroke="#b81d85" stroke-width="3"/></svg>Construction and Property</li>
    <li><svg width="18" height="14" viewBox="0 0 18 14"><path d="M1 7 H15 M9 1 L15 7 L9 13" fill="none" stroke="#b81d85" stroke-width="3"/></svg>Accounting</li>
    <li><svg width="18" height="14" viewBox="0 0 18 14"><path d="M1 7 H15 M9 1 L15 7 L9 13" fill="none" stroke="#b81d85" stroke-width="3"/></svg>Customer Service</li>
    <li><svg width="18" height="14" viewBox="0 0 18 14"><path d="M1 7 H15 M9 1 L15 7 L9 13" fill="none" stroke="#b81d85" stroke-width="3"/></svg>Data Entry</li>
    <li><svg width="18" height="14" viewBox="0 0 18 14"><path d="M1 7 H15 M9 1 L15 7 L9 13" fill="none" stroke="#b81d85" stroke-width="3"/></svg>Cell Centre</li>
    <li><svg width="18" height="14" viewBox="0 0 18 14"><path d="M1 7 H15 M9 1 L15 7 L9 13" fill="none" stroke="#b81d85" stroke-width="3"/></svg>Project Engineering</li>
  </ul>
</div>

<aside class="news abs" lang="en">
  <h2>Latest News</h2>
  <p>Lorem ipsum dolor sit amet, con&shy;sectetur adipisicing elit, sed do eiusmod tempor incididunt ut labore et dolore magna aliqua. Ut enim ad minim veniam, quis nos&shy;trud exercitation ullamco laboris nisi ut aliquip ex ea commodo con&shy;sequat. Duis aute irure dolor in reprehenderit in voluptate velit esse cillum dolore eu fugiat nulla pariatur.</p>
  <a href="#">readmore →</a>
</aside>

<footer class="site-footer abs">
  <div class="footer-title abs" style="left:92px">FIND US ON MAP</div>
  <div class="footer-title abs" style="left:594px">LINKS</div>
  <div class="footer-title abs" style="left:913px">FOLLOW US</div>
  <div class="footer-rule abs"></div>
  <div class="map abs" role="img" aria-label="Street map showing the office location with a marker pin"></div>
  <div class="address abs">
    Level 5, 7 Pemberly Terrace<br>
    SUBIACO WA 6008<br>
    <b>Phone</b> - (08) 9271 5608<br>
    <b>Fax</b> - (08) 9271 5690<br>
    <b>Email</b> - admin@calderbrook.com.au
  </div>
  <ul class="links abs" style="left:594px;top:58px">
    <li>Home</li><li>About Us</li><li>Services</li><li>The Team</li><li>Key Contacts</li><li>Our Values</li><li>Send Resume</li>
  </ul>
  <ul class="links abs" style="left:748px;top:57px">
    <li>Timesheets</li><li>Candidates</li><li>Clients</li><li>Location</li><li>Contact Us</li>
  </ul>
  <ul class="follow abs">
    <li><span></span>Friendnest</li>
    <li><span></span>Chirpline</li>
    <li><span></span>Clipstream</li>
    <li><span></span>Workcircle</li>
  </ul>
  <div class="footer-rule bottom abs"></div>
  <div class="copyright abs">Copyright © 2012 Calderbrook - The Recruitment Bureau, All rights reserved!</div>
</footer>

</body>
</html>
```